Jamaica Castor Oil - Label design

Design brief for Labels:

Castor oil has been used for centuries as one of the best products for hair care, and it is well recognized that Jamaica Black Castor Oil is rated as the best in the world. We will sell cold pressed Jamaica castor oil online using modern packaging. The product is one of the best natural products for hair regrowth, to correct spit ends, reduce dandruff, and create healthy hair. We will target, women, particularly women of Caribbean origin, and African American women.

1. The focus of this project will be to distribute the product online via our website in the first instance, and then distribute the product to Hairdressers and Hair Care professionals in the second instance. The website address must feature clearly and prominently on the front panel of the label, so if someone tries the product and wants to re-order they can easily see the website.
2. The label must seem “natural” and “from the farm”- the type of product used and trusted for half a century + in Jamaica, which the world is just discovering.
3. The brand is MarloweGrovz and the logo should be placed in the top center of the label. (log is attached)
4. The “Black” in the front panel of the label has to be emphasized with different typestyle.
5. Bottle being used will be PET Green with Yorker spout cap.
6. Bottle size (see attached) diagram
7. Label Size will be 4.625” (height) x 5.687 (width)
8. If the project is successful, we plan product extensions within the Castor Oil area, and also additional hair care natural products.

See pictures attached"
1. Picture of the bottle to be used.
2. Picture of the filled bottle, with label (no design), with content written on it.
3. Label, with all wording required.
4. Logo which will be used for the company - Marlowegrovz
5. Diagram with all bottle dimensions
---------------------------------------------------------------
Note that the circumference of the bottle is 6 inches
The label will be self adhesive and will not require any overlap

Target Market(s)

The target market will be Caribbean women, and also African American Women - they focus on their hair, and always want the hair to look and feel great. - This is a natural product and gives them great results - many of these women (especially the Caribbean women) would have used castor Oil in their hair as a child but no longer use it as an adult - Traditionally the product had a very bad odor, but was very effective, but our brand uses more modern processing techniques to give better results without the odor.

Industry/Entity Type

Hair

Requirements
Must have
• Important to feature website on label for re-ordering.

```html
<!DOCTYPE html>
<html lang="en">
<head>
<meta charset="utf-8">
<title>MarloweGrovz Black Castor Oil – Label Set</title>
<link href="https://fonts.googleapis.com/css2?family=Tulpen+One&family=Roboto+Condensed:wght@400;500&display=swap" rel="stylesheet">
<style>
  :root {
    --page: #ffffff;
    --slate-top: #585e60;
    --slate-bottom: #3f4446;
    --navy-top: #26344a;
    --navy-bottom: #18212f;
    --orange: #e4661f;
    --blue: #3f86e0;
    --white: #ffffff;
    --soft-white: #e6e9ea;
    --logo-grey: #8e9597;
    --logo-navy: #8793a6;
    --palm: #f4f4f4;
  }
  * { box-sizing: border-box; margin: 0; padding: 0; }
  html, body { width: 1200px; height: 1200px; overflow: hidden; background: var(--page); }
  .canvas {
    width: 1200px; height: 1200px; position: relative;
    display: flex; justify-content: center; align-items: center; gap: 48px;
  }
  .label {
    width: 240px; height: 580px; position: relative; overflow: hidden;
    font-family: "Roboto Condensed", sans-serif; color: var(--white); text-align: center;
  }
  .label--slate { background: linear-gradient(180deg, var(--slate-top), var(--slate-bottom)); --accent: var(--orange); --logo: var(--logo-grey); }
  .label--navy  { background: linear-gradient(180deg, var(--navy-top), var(--navy-bottom)); --accent: var(--blue); --logo: var(--logo-navy); }

  .brand { position: absolute; top: 26px; left: 0; right: 0; display: flex; flex-direction: column; align-items: center; gap: 4px; }
  .brand__dot { width: 26px; height: 26px; border-radius: 50%; background: var(--logo); }
  .brand__name { font-size: 12px; color: var(--logo); letter-spacing: 0.2px; }

  .palm-art {
    position: absolute; top: 96px; left: 62px; width: 110px; height: 76px;
    background: radial-gradient(ellipse at 50% 65%, var(--palm) 0%, rgba(244,244,244,0.55) 45%, rgba(244,244,244,0) 72%);
  }
  .seal {
    position: absolute; top: 146px; left: 164px; width: 54px; height: 54px;
    border: 2px solid var(--accent); border-radius: 50%; opacity: 0.85;
  }

  .title { font-weight: 400; }
  .title__line {
    position: absolute; left: 0; right: 0;
    display: flex; justify-content: center; align-items: center;
    font-family: "Tulpen One", sans-serif; line-height: 1; white-space: nowrap;
  }
  .title__line span { display: inline-block; transform-origin: center; }
  .title__region { top: 178px; height: 62px; font-size: 80px; color: var(--accent); }
  .title__region span { transform: scaleX(0.78); letter-spacing: 3px; }
  .title__black {
    top: 241px; height: 123px; font-size: 160px; color: var(--white);
    border-top: 1px solid rgba(255,255,255,0.25); border-bottom: 1px solid var(--accent);
    left: 20px; right: 20px;
  }
  .title__black span { transform: scaleX(0.7); letter-spacing: 6px; }
  .title__product { top: 366px; height: 58px; font-size: 78px; color: var(--accent); }
  .title__product span { transform: scaleX(0.8); letter-spacing: 3px; }

  .tagline { position: absolute; top: 430px; left: 0; right: 0; font-size: 14px; line-height: 16px; letter-spacing: 0.8px; color: var(--soft-white); }

  .web { position: absolute; top: 498px; left: 0; right: 0; font-size: 13.5px; letter-spacing: 0.6px; color: var(--accent); }
  .origin { position: absolute; top: 526px; left: 0; right: 0; font-size: 13.5px; letter-spacing: 1px; color: var(--soft-white); }
  .size { position: absolute; top: 553px; left: 0; right: 0; font-size: 13px; color: var(--soft-white); }

  .copy {
    position: absolute; top: 116px; left: 24px; right: 16px; text-align: left;
    font-size: 9.5px; line-height: 13.6px; color: var(--soft-white); letter-spacing: 0.3px;
  }
  .copy p + p { margin-top: 14px; }
</style>
</head>
<body>
<main class="canvas">

  <section class="label label--slate" aria-label="Front label, slate">
    <div class="brand"><span class="brand__dot"></span><span class="brand__name">MarloweGrovz</span></div>
    <div class="palm-art" role="img" aria-label="White palm trees on a small island"></div>
    <div class="seal" role="img" aria-label="Round stamp badge"></div>
    <h1 class="title">
      <div class="title__line title__region"><span>JAMAICA</span></div>
      <div class="title__line title__black"><span>BLACK</span></div>
      <div class="title__line title__product"><span>CASTOR OIL</span></div>
    </h1>
    <p class="tagline">UNREFINED AND INFUSED<br>WITH VIRGIN COCONUT OIL</p>
    <p class="web">WWW.ISLANDROOTOIL.COM</p>
    <p class="origin">– PRODUCT OF JAMAICA –</p>
    <p class="size">8oz</p>
  </section>

  <section class="label label--slate" aria-label="Back label, slate">
    <div class="brand"><span class="brand__dot"></span><span class="brand__name">MarloweGrovz</span></div>
    <div class="copy">
      <p>Cold pressed from roasted castor beans grown on small family farms in the Jamaican hills, this oil is made the way it has been for generations. Massage a few drops into the scalp and along the length of the hair to nourish roots, soften ends and calm dryness.</p>
      <p>Infused with virgin coconut oil for a lighter feel and a clean, gentle scent. Leave on overnight or use as a pre-wash treatment, then rinse.</p>
      <p>Ingredients: Ricinus communis seed oil, Cocos nucifera oil. For external use only.</p>
    </div>
    <p class="web">WWW.ISLANDROOTOIL.COM</p>
    <p class="origin">– PRODUCT OF JAMAICA –</p>
  </section>

  <section class="label label--navy" aria-label="Front label, navy">
    <div class="brand"><span class="brand__dot"></span><span class="brand__name">MarloweGrovz</span></div>
    <div class="palm-art" role="img" aria-label="White palm trees on a small island"></div>
    <div class="seal" role="img" aria-label="Round stamp badge"></div>
    <h1 class="title">
      <div class="title__line title__region"><span>JAMAICA</span></div>
      <div class="title__line title__black"><span>BLACK</span></div>
      <div class="title__line title__product"><span>CASTOR OIL</span></div>
    </h1>
    <p class="tagline">UNREFINED AND INFUSED<br>WITH VIRGIN COCONUT OIL</p>
    <p class="web">WWW.ISLANDROOTOIL.COM</p>
    <p class="origin">– PRODUCT OF JAMAICA –</p>
    <p class="size">8oz</p>
  </section>

  <section class="label label--navy" aria-label="Back label, navy">
    <div class="brand"><span class="brand__dot"></span><span class="brand__name">MarloweGrovz</span></div>
    <div class="copy">
      <p>Cold pressed from roasted castor beans grown on small family farms in the Jamaican hills, this oil is made the way it has been for generations. Massage a few drops into the scalp and along the length of the hair to nourish roots, soften ends and calm dryness.</p>
      <p>Infused with virgin coconut oil for a lighter feel and a clean, gentle scent. Leave on overnight or use as a pre-wash treatment, then rinse.</p>
      <p>Ingredients: Ricinus communis seed oil, Cocos nucifera oil. For external use only.</p>
    </div>
    <p class="web">WWW.ISLANDROOTOIL.COM</p>
    <p class="origin">– PRODUCT OF JAMAICA –</p>
  </section>

</main>
</body>
</html>
```